Printing company needs website!

A printing company would like a new professional website (made with wix). Now they don't have a website, but they want a unique, beautiful, clear site. Of course they provide the content themselves, we are now looking for the beautiful design with some mockups. You can see several of their projects on their instagram & facebook.
Www.kwelmast.com/brimvelt and https://www.fotoravel.com/brimvelt.be/ logos are attached.

```html
<!DOCTYPE html>
<html lang="en">
<head>
<meta charset="utf-8">
<title>Brimvelt – Printing Services</title>
<link rel="stylesheet" href="https://fonts.googleapis.com/css2?family=Poppins:wght@300;400;500;600;700;800&display=swap">
<style>
:root{
  --teal:#33b5aa;
  --teal-dark:#24948b;
  --yellow:#f5c000;
  --blue:#1ba6dc;
  --ink:#2b2b2b;
  --grey:#6f6f6f;
  --light:#f4f8f8;
  --white:#ffffff;
}
*{margin:0;padding:0;box-sizing:border-box}
html,body{width:1200px;height:4451px;overflow:hidden}
body{font-family:'Poppins',sans-serif;color:var(--ink);background:var(--white);position:relative}
.abs{position:absolute}
.ph{position:absolute}
.btn{position:absolute;display:flex;align-items:center;justify-content:center;font-weight:600;font-size:13px;letter-spacing:.5px;text-transform:uppercase}
/* header */
.hero{left:0;top:0;width:1200px;height:704px;background:linear-gradient(120deg,#3c4a50 0%,#56666c 45%,#2f3c40 100%)}
.hero-accent{left:620px;top:130px;width:520px;height:520px;border-radius:50%;background:radial-gradient(circle at 45% 45%,rgba(230,90,170,.55),rgba(60,190,170,.35) 55%,rgba(0,0,0,0) 70%)}
.topbar{left:0;top:0;width:1200px;height:78px;background:rgba(30,45,50,.55);border-bottom:1px solid rgba(255,255,255,.15)}
.logo{display:flex;align-items:center;gap:10px;font-weight:700}
.logo .dot{width:34px;height:34px;border-radius:50%;background:var(--teal)}
.nav a{position:absolute;top:33px;color:#fff;font-size:12px;text-decoration:none;letter-spacing:.3px}
.nav .active{border-bottom:2px solid var(--teal);padding-bottom:25px}
.phone{left:954px;top:24px;width:165px;height:37px;background:var(--teal);color:#fff;border-radius:20px;font-size:14px;gap:8px}
.hero-welcome{left:121px;top:234px;color:#fff;font-weight:400;font-size:25px;line-height:32px}
.hero-title{left:119px;top:268px;color:#fff;font-weight:800;font-size:57px;line-height:62px}
.hero-title span{color:var(--teal)}
.dots{left:556px;top:665px;display:flex;gap:9px}
.dots i{width:12px;height:12px;border-radius:50%;background:#fff;display:block}
.dots i.on{background:var(--yellow)}
/* about */
.about-photo{left:143px;top:790px;width:512px;height:393px;background:linear-gradient(135deg,#c9cfd2,#8e989c 60%,#d6dadb)}
.about-frame{left:678px;top:895px;width:391px;height:265px;border-right:4px solid var(--teal);border-bottom:4px solid var(--teal)}
.about-card{left:598px;top:825px;width:467px;height:330px;background:#fff;box-shadow:0 6px 30px rgba(0,0,0,.12);padding:36px 48px}
.eyebrow{color:var(--teal);font-size:14px;letter-spacing:.5px;text-transform:uppercase}
.about-card h2{font-size:27px;font-weight:700;margin:4px 0 12px}
.about-card p{font-size:12px;color:var(--grey);line-height:23px;margin-bottom:12px}
.outline-btn{border:2px solid var(--teal);color:var(--teal);border-radius:24px;background:#fff}
/* services */
.services{left:0;top:1266px;width:1200px;height:503px;background:var(--light)}
.center-t{width:1200px;text-align:center}
.services h2{font-size:30px;font-weight:600}
.svc-icon{width:84px;height:84px;border-radius:50%;background:#fff;box-shadow:0 4px 14px rgba(0,0,0,.08);display:flex;align-items:center;justify-content:center}
.svc h3{color:var(--teal);font-size:17px;font-weight:600}
.svc p{font-size:11px;color:var(--grey);line-height:18px;margin-top:6px}
.svc.right{text-align:left}.svc.left{text-align:right}
/* split */
.split-text{color:#fff;text-align:center}
.split-text .eyebrow{color:#fff;font-size:15px}
.split-text h2{font-size:33px;font-weight:600;margin:6px 0 10px}
.split-text p{font-size:13px;font-weight:600;line-height:23px}
.white-btn{background:#fff;border-radius:20px;color:var(--teal)}
/* why */
.why h2{font-size:32px;font-weight:400}
.why h2 b{font-weight:700}
.feature{display:flex;align-items:center;gap:22px}
.feature .ic{width:82px;height:82px;border-radius:50%;border:2px solid var(--teal);display:flex;align-items:center;justify-content:center;flex:none}
.feature .ic.y{border-color:var(--yellow)}
.feature h3{font-size:16px;font-weight:700}
.feature p{font-size:12px;color:var(--grey)}
/* gallery */
.gallery{left:0;top:2918px;width:1200px;height:623px;background-color:#f6fafb;background-image:linear-gradient(#e4eef0 1px,transparent 1px),linear-gradient(90deg,#e4eef0 1px,transparent 1px);background-size:22px 22px}
.gallery .eyebrow{text-transform:none;font-size:19px}
.gallery h2{font-size:36px;font-weight:400}
.gallery h2 b{font-weight:700}
.gallery-photo{left:124px;top:3103px;width:512px;height:329px;border-radius:6px;background:linear-gradient(135deg,#f2c200 0%,#e9b800 55%,#2aa6d8 100%)}
.gal-text h3{font-size:19px;font-weight:600;line-height:33px;color:#444}
.gal-text p{font-size:15px;color:var(--grey);line-height:32px;margin-top:10px}
/* contact */
.contact{left:0;top:3541px;width:1200px;height:565px;background:linear-gradient(120deg,#1fa29f,#36b8ae)}
.contact-kicker{left:138px;top:3646px;color:#fff;font-weight:400;font-size:20px;line-height:26px}
.contact-title{left:138px;top:3672px;color:#fff;font-size:38px;font-weight:400;line-height:48px}
.contact-title b{font-weight:700}
.field{background:#fff;font-size:11px;color:#777;padding:12px 15px}
.send{background:var(--yellow);color:#fff;border-radius:22px}
/* footer */
.foot-col h4{font-size:14px;font-weight:700;border-left:3px solid var(--yellow);padding-left:14px;height:22px;line-height:22px}
.foot-col a{display:block;font-size:11px;color:#444;text-decoration:none;margin:14px 0 0 16px}
.contact-row{display:flex;gap:14px;margin:16px 0 0 16px;font-size:13px;color:#333;align-items:flex-start}
.contact-row small{display:block;font-size:10px;color:#555}
.social{width:34px;height:34px;border-radius:50%;background:var(--teal)}
.copy{left:0;top:4416px;width:1200px;text-align:center;font-size:12px;color:#666}
</style>
</head>
<body>

<!-- HERO -->
<div class="ph hero" role="img" aria-label="Photo of an industrial printing press running a colourful print roll"></div>
<div class="ph hero-accent" role="img" aria-label="Colour print roll highlight"></div>
<header class="abs topbar">
  <div class="abs logo" style="left:104px;top:20px;color:#fff;font-size:30px"><span class="dot"></span>Brimvelt</div>
  <nav class="nav">
    <a class="active" style="left:388px">ABOUT US</a>
    <a style="left:492px">OUR SERVICES</a>
    <a style="left:621px">PRINTING</a>
    <a style="left:720px">OUR WORK</a>
    <a style="left:831px">CONTACT US</a>
  </nav>
  <div class="btn phone">
    <svg width="18" height="18" viewBox="0 0 24 24"><circle cx="12" cy="12" r="12" fill="#fff"/><path d="M8 6l2 0 1 3-1.5 1a8 8 0 0 0 4.5 4.5l1-1.5 3 1v2a2 2 0 0 1-2 2A11 11 0 0 1 6 8a2 2 0 0 1 2-2z" fill="#33b5aa"/></svg>
    0412 5539 27
  </div>
</header>
<p class="abs hero-welcome">Welcome to Brimvelt</p>
<h1 class="abs hero-title">BEST PRINTING<br><span>SERVICES</span></h1>
<div class="btn" style="left:121px;top:412px;width:176px;height:46px;background:var(--blue);color:#fff">Request Quote</div>
<div class="btn" style="left:306px;top:412px;width:175px;height:46px;border:2px solid #fff;color:#fff">Learn More</div>
<div class="abs dots"><i></i><i></i><i></i><i class="on"></i></div>

<!-- ABOUT -->
<div class="ph about-photo" role="img" aria-label="Smiling print technician standing beside a printing machine"></div>
<div class="abs about-frame"></div>
<div class="abs about-card">
  <div class="eyebrow">Who we are <span style="display:inline-block;width:40px;height:1px;background:var(--teal);vertical-align:middle;margin-left:6px"></span></div>
  <h2>ABOUT BRIMVELT</h2>
  <p>Lorem ipsum dolor sit amet, consectetur adipiscing elit, sed do eiusmod tempor incididunt ut labore et dolore magna aliqua. Ut enim ad minim veniam, quis nostrud exercitation</p>
  <p>Auis aute irure dolor in reprehenderit in voluptate velit esse cillum dolore eu fugiat nulla pariatur.</p>
</div>
<div class="btn outline-btn" style="left:646px;top:1068px;width:155px;height:41px">Learn More</div>

<!-- SERVICES -->
<section class="abs services">
  <div class="abs center-t eyebrow" style="top:52px">What we do</div>
  <h2 class="abs center-t" style="top:76px">PRINTING SERVICES</h2>
</section>
<svg class="abs" style="left:0;top:1266px" width="1200" height="503">
  <g fill="none" stroke="var(--teal)" stroke-width="1.5">
    <circle cx="600" cy="295" r="138"/>
    <path d="M443 186 L470 186 L496 207"/><path d="M443 390 L470 390 L496 375"/>
    <path d="M765 186 L738 186 L710 207"/><path d="M765 390 L738 390 L710 375"/>
  </g>
  <g fill="var(--teal)"><circle cx="496" cy="207" r="4"/><circle cx="496" cy="375" r="4"/><circle cx="710" cy="207" r="4"/><circle cx="710" cy="375" r="4"/></g>
  <circle cx="600" cy="295" r="118" fill="#fff" style="filter:drop-shadow(0 4px 14px rgba(0,0,0,.1))"/>
  <circle cx="600" cy="295" r="18" fill="var(--teal)"/>
</svg>
<div class="abs svc-icon" style="left:359px;top:1410px"><svg width="40" height="40" viewBox="0 0 40 40" fill="none" stroke="var(--teal)" stroke-width="1.6"><rect x="6" y="8" width="28" height="24" rx="2"/><path d="M12 16h16M12 22h10"/></svg></div>
<div class="abs svc-icon" style="left:359px;top:1614px"><svg width="40" height="40" viewBox="0 0 40 40" fill="none" stroke="var(--teal)" stroke-width="1.6"><path d="M6 10l9-3 10 3 9-3v23l-9 3-10-3-9 3z"/><path d="M15 7v23M25 10v23"/></svg></div>
<div class="abs svc-icon" style="left:765px;top:1410px"><svg width="40" height="40" viewBox="0 0 40 40" fill="none" stroke="var(--teal)" stroke-width="1.6"><rect x="6" y="9" width="28" height="22" rx="2"/><path d="M9 27l8-8 6 6 4-4 5 5"/></svg></div>
<div class="abs svc-icon" style="left:765px;top:1614px"><svg width="40" height="40" viewBox="0 0 40 40" fill="none" stroke="var(--teal)" stroke-width="1.6"><path d="M20 6l13 7v14l-13 7-13-7V13z"/><path d="M7 13l13 7 13-7M20 20v14"/></svg></div>
<div class="abs svc left" style="left:110px;top:1430px;width:214px"><h3>Poster Printing</h3><p>Lorem ipsum dolor sit amet, consect-etur adipiscing elit, sed do eius</p></div>
<div class="abs svc left" style="left:100px;top:1611px;width:228px"><h3>Brochure Printing</h3><p>Lorem ipsum dolor sit amet, consectetur adipiscing elit, sed do eiusmod</p></div>
<div class="abs svc right" style="left:867px;top:1426px;width:220px"><h3>Card Printing</h3><p>Lorem ipsum dolor sit amet, consect-etur adipiscing elit, sed do eiusmov</p></div>
<div class="abs svc right" style="left:867px;top:1624px;width:225px"><h3>Product Printing</h3><p>Lorem ipsum dolor sit amet, consectetur adipiscing elit, sed do eiusmod temp</p></div>

<!-- SPLIT -->
<svg class="abs" style="left:0;top:1769px" width="1200" height="544" role="img" aria-label="Tinted photos of printing machinery">
  <polygon points="0,0 593,50 593,487 0,544" fill="var(--yellow)"/>
  <polygon points="593,50 1200,0 1200,544 593,487" fill="var(--blue)"/>
</svg>
<div class="abs split-text" style="left:130px;top:1958px;width:404px">
  <div class="eyebrow">What we do</div><h2>PRINTING MACHINE</h2>
  <p>Lorem ipsum dolor sit amet, consectetur adipiscing elit, sed do eiusmod tempor incididunt ut</p>
</div>
<div class="btn white-btn" style="left:267px;top:2106px;width:152px;height:36px">Learn More</div>
<div class="abs split-text" style="left:683px;top:1962px;width:404px">
  <div class="eyebrow">What we do</div><h2>BOOK YOUR PRINTING</h2>
  <p>Lorem ipsum dolor sit amet, consectetur adipiscing elit, sed do eiusmod tempor incididunt ut</p>
</div>
<div class="btn white-btn" style="left:809px;top:2106px;width:152px;height:36px">Learn More</div>

<!-- WHY -->
<div class="abs why" style="left:137px;top:2398px">
  <h2>Why choose <b>Brimvelt</b></h2>
  <div style="width:74px;height:3px;background:var(--teal);margin-top:12px"></div>
</div>
<div class="abs feature" style="left:125px;top:2492px"><div class="ic"><svg width="38" height="38" viewBox="0 0 40 40" fill="none" stroke="var(--teal)" stroke-width="1.6"><circle cx="20" cy="16" r="10"/><path d="M14 25l-3 10 9-4 9 4-3-10"/></svg></div><div><h3>QUALITY PRINTING</h3><p>Lorem ipsum dolor sit amet consectetur</p></div></div>
<div class="abs feature" style="left:125px;top:2610px"><div class="ic y"><svg width="38" height="38" viewBox="0 0 40 40" fill="none" stroke="var(--yellow)" stroke-width="1.6"><rect x="8" y="10" width="24" height="20"/><path d="M8 16h24M14 10v20M26 10v20"/></svg></div><div><h3>FLEXIBLE PRICING</h3><p>Lorem ipsum dolor sit amet consectetur</p></div></div>
<div class="abs feature" style="left:125px;top:2726px"><div class="ic"><svg width="38" height="38" viewBox="0 0 40 40" fill="none" stroke="var(--teal)" stroke-width="1.6"><rect x="10" y="6" width="18" height="24"/><path d="M14 12h10M14 17h10M8 22h24v10H8z"/></svg></div><div><h3>OFFSET PRINTING</h3><p>Lorem ipsum dolor sit amet consectetur</p></div></div>
<div class="ph" style="left:787px;top:2464px;width:310px;height:310px;border-radius:50%;background:#d4eeea"></div>
<div class="ph" style="left:596px;top:2377px;width:239px;height:211px;background:linear-gradient(135deg,#3b3f44,#8a5a55 55%,#c9c2bd)" role="img" aria-label="Close-up of a large-format printer head"></div>
<div class="ph" style="left:852px;top:2488px;width:239px;height:211px;background:linear-gradient(135deg,#9aa3a6,#d8dadb 45%,#e69a3a 75%,#3a8fc8)" role="img" aria-label="Paper roll running through press cylinders"></div>
<div class="ph" style="left:596px;top:2606px;width:239px;height:209px;background:linear-gradient(135deg,#2a2c30,#5a5d62 50%,#d35a8a 80%,#3bb0c8)" role="img" aria-label="Colour calibration strips on a printer"></div>

<!-- GALLERY -->
<section class="abs gallery">
  <div class="abs center-t eyebrow" style="top:56px">Project Gallery</div>
  <h2 class="abs center-t" style="top:82px">Our <b>Printing</b> Work</h2>
  <div class="abs" style="left:564px;top:136px;width:74px;height:3px;background:var(--teal)"></div>
</section>
<div class="ph gallery-photo" role="img" aria-label="Project showcase: courier handing over a parcel beside a branded yellow delivery van, set in a decorative colour frame"></div>
<div class="abs gal-text" style="left:683px;top:3143px;width:380px">
  <h3>Sed ut perspiciatis unde omnis iste natus error sit voluptatem ac</h3>
  <p>Lorem ipsum dolor sit amet, consectetur adipi-scing elit, sed do eiusmod tempor incididunt ut labore et dolore magna aliqua.</p>
</div>
<div class="btn outline-btn" style="left:686px;top:3347px;width:154px;height:39px;background:transparent">Learn More</div>

<!-- CONTACT -->
<section class="abs contact"></section>
<svg class="abs" style="left:596px;top:3541px" width="604" height="565" role="img" aria-label="Photo of printed sheets speeding through a rotary press">
  <defs><linearGradient id="press" x1="0" y1="0" x2="1" y2="1"><stop offset="0" stop-color="#5b6570"/><stop offset=".5" stop-color="#c9ccd0"/><stop offset=".8" stop-color="#b8526a"/><stop offset="1" stop-color="#3f4a55"/></linearGradient></defs>
  <polygon points="160,0 604,0 604,565 160,565 0,283" fill="url(#press)"/>
</svg>
<p class="abs contact-kicker">Get in touch</p>
<h2 class="abs contact-title"><b>Contact</b> Us</h2>
<div class="abs field" style="left:138px;top:3740px;width:216px;height:41px">First Name</div>
<div class="abs field" style="left:361px;top:3740px;width:218px;height:41px">Last Name</div>
<div class="abs field" style="left:138px;top:3786px;width:216px;height:42px">Phone Number</div>
<div class="abs field" style="left:361px;top:3786px;width:218px;height:42px">Email address</div>
<div class="abs field" style="left:138px;top:3838px;width:441px;height:76px">Message</div>
<div class="btn send" style="left:135px;top:3932px;width:174px;height:43px">Send Enquiry</div>

<!-- FOOTER -->
<div class="abs logo" style="left:130px;top:4190px;color:var(--ink);font-size:40px"><span class="dot" style="width:54px;height:54px"></span>Brimvelt</div>
<div class="abs" style="left:182px;top:4271px;display:flex;gap:8px"><span class="social"></span><span class="social"></span><span class="social"></span><span class="social"></span></div>
<div class="abs foot-col" style="left:446px;top:4170px"><h4>NAVIGATION</h4><a>About Us</a><a>Printing Services</a><a>Why We Are</a><a>Testimonials</a></div>
<div class="abs foot-col" style="left:654px;top:4170px"><h4>RESOURCES</h4><a>Our Work</a><a>Blogs</a><a>Contact Us</a><a>Privacy Policy</a></div>
<div class="abs foot-col" style="left:870px;top:4170px"><h4>CONTACT US</h4>
  <div class="contact-row"><svg width="18" height="18" viewBox="0 0 24 24" fill="none" stroke="var(--teal)" stroke-width="1.8"><path d="M6 3l3 0 1.5 4-2 1.5a10 10 0 0 0 5 5l1.5-2 4 1.5v3a2 2 0 0 1-2 2A16 16 0 0 1 4 5a2 2 0 0 1 2-2z"/></svg><div><small>Phone</small>0412 5539 27</div></div>
  <div class="contact-row"><svg width="18" height="18" viewBox="0 0 24 24" fill="none" stroke="var(--teal)" stroke-width="1.8"><circle cx="12" cy="12" r="9"/><path d="M3 12h18M12 3c3 3 3 15 0 18M12 3c-3 3-3 15 0 18"/></svg><div style="font-size:11px"><small>Website</small>www.brimvelt.be</div></div>
  <div class="contact-row"><svg width="18" height="18" viewBox="0 0 24 24" fill="none" stroke="var(--teal)" stroke-width="1.8"><rect x="3" y="6" width="18" height="12"/><path d="M3 6l9 7 9-7"/></svg><div style="font-size:11px"><small>Email</small>info@brimvelt.be</div></div>
</div>
<div class="abs copy">Copyright © 2022 Brimvelt All Right Reserved</div>

</body>
</html>
```